Career development coaching - school lever to adults, needs a business card

Tandem Lark - An independent Career Advice business that provides 1-2-1 advice,for career development, entrepreneurial support and workshops needs a business card. Our clients of all ages (school leaver to adults looking for a career move) and universities and colleges. We would like the card to be double-sided with a modern, professional look. Looking for something professional yet very creative and original. Want a standard size business card that inspires a second look because it stands out from the rest.

One side of the card to have a design incorporating the logo with Tandem Lark name with the strap line “Helping you find your future” and space for the company website

Other side of the card to the logo/Tandem Lark name and the usual contact information:
Individual Name
Job Title (for example, Director)
Phone number
Email address
Company website address

Facebook, LinkedIn and Twitter links will need to go somewhere (back or front!)

The design will be used for 3 individuals so should be editable so that we can update as needed/as we grow.

Attached is the company logo/colours to be incorporated.

Target Market(s)

1-2-1 advice,for career development, entrepreneurial support and workshops needs a business card. Our clients of all ages (school leaver to adults looking for a career move) and universities and colleges.

Industry/Entity Type

Consulting

Contact Information for Business Card

Individual Name
Phone number
Email address
Company website address

Font styles to use
Sans Serif

Colors
0255a3
3176b5
faa54b
f78f20
85acd3
cfdeed

Requirements
Must have
• use the Tandem Lark Logo in some way - using the colours and the blue/orange palette
• For the logo - hope this makes sense to someone or if they direclty relate to the logo image attached!
• For the Orange:- Pantone 1585 C
• In CMYK : C3 M71 Y100 K0
• For the Blue:- 100% Pantone 7469 C
• In CMYK : C100 M62 Y27 K7
• Please feel free to contact me with any questions for more info
Nice to have
• happy to see any creative designs
Should not have
• Nothing too traditional,

```html
<!DOCTYPE html>
<html lang="en">
<head>
<meta charset="utf-8">
<title>Tandem Lark – Business Card</title>
<link href="https://fonts.googleapis.com/css2?family=Roboto:wght@400;500&display=swap" rel="stylesheet">
<style>
  :root {
    --stage: #5b5b5d;
    --card-dark: #3e3e40;
    --card-light: #ffffff;
    --brand-blue: #1a6690;
    --brand-orange: #f07232;
    --accent-orange: #f6a445;
    --ink: #2b2b2b;
    --rule: #3a3a3a;
  }
  * { box-sizing: border-box; margin: 0; padding: 0; }
  html, body { width: 1200px; height: 1200px; overflow: hidden; }
  body {
    background: var(--stage);
    font-family: "Roboto", Arial, sans-serif;
    position: relative;
  }
  .card {
    position: absolute;
    left: 253px;
    width: 695px;
    height: 394px;
  }
  .card--front { top: 178px; background: var(--card-dark); }
  .card--back { top: 629px; background: var(--card-light); }

  .brand-dot {
    position: absolute;
    border-radius: 50%;
    background: var(--brand-blue);
  }
  .brand-name {
    position: absolute;
    font-weight: 500;
    color: var(--brand-orange);
    letter-spacing: 1px;
    text-transform: uppercase;
    white-space: nowrap;
    transform: translateX(-50%);
  }

  .card--front .brand-dot { width: 130px; height: 130px; left: 282px; top: 53px; }
  .card--front .brand-name { left: 347px; top: 210px; font-size: 36px; }
  .tagline {
    position: absolute;
    left: 0; right: 0;
    top: 292px;
    text-align: center;
    font-size: 22px;
    color: var(--accent-orange);
  }
  .social {
    position: absolute;
    top: 342px;
    left: 0; right: 0;
    display: flex;
    justify-content: center;
    gap: 11px;
  }
  .social__link {
    width: 29px; height: 29px;
    background: var(--accent-orange);
    border-radius: 2px;
  }

  .card--back .brand-dot { width: 116px; height: 116px; left: 105px; top: 113px; }
  .card--back .brand-name { left: 163px; top: 245px; font-size: 32px; }
  .divider {
    position: absolute;
    left: 308px; top: 83px;
    width: 1px; height: 228px;
    background: var(--rule);
  }
  .person { position: absolute; left: 335px; top: 118px; }
  .person__name { font-size: 28px; color: var(--brand-blue); line-height: 1.2; }
  .person__role { font-size: 21px; color: var(--ink); line-height: 1.25; }
  .contact {
    position: absolute;
    left: 343px; top: 196px;
    list-style: none;
  }
  .contact__item {
    display: flex;
    align-items: center;
    gap: 12px;
    font-size: 22px;
    color: var(--ink);
    height: 26.5px;
  }
  .contact__icon { width: 19px; height: 19px; flex: none; }
</style>
</head>
<body>
  <section class="card card--front" aria-label="Card front">
    <span class="brand-dot" aria-hidden="true"></span>
    <h1 class="brand-name">Tandem Lark</h1>
    <p class="tagline">Helping you find your future</p>
    <nav class="social" aria-label="Social links">
      <span class="social__link" aria-label="Social profile 1"></span>
      <span class="social__link" aria-label="Social profile 2"></span>
      <span class="social__link" aria-label="Social profile 3"></span>
    </nav>
  </section>

  <section class="card card--back" aria-label="Card back">
    <span class="brand-dot" aria-hidden="true"></span>
    <h2 class="brand-name">Tandem Lark</h2>
    <span class="divider" aria-hidden="true"></span>
    <div class="person">
      <p class="person__name">Maren Holt</p>
      <p class="person__role">Director</p>
    </div>
    <ul class="contact">
      <li class="contact__item">
        <svg class="contact__icon" viewBox="0 0 20 20" aria-hidden="true">
          <path d="M2 8c0-3 4-5 8-5s8 2 8 5l-4 1-1-2H7L6 9z" fill="var(--brand-orange)"/>
          <rect x="4" y="10" width="12" height="7" rx="1.5" fill="var(--brand-orange)"/>
          <circle cx="10" cy="13.5" r="2" fill="#fff"/>
        </svg>
        00-000-0000
      </li>
      <li class="contact__item">
        <svg class="contact__icon" viewBox="0 0 20 20" aria-hidden="true">
          <rect x="1" y="4" width="18" height="12" fill="var(--brand-orange)"/>
          <path d="M1 4l9 7 9-7M1 16l7-6M19 16l-7-6" stroke="#fff" stroke-width="1.4" fill="none"/>
        </svg>
        mholt@tandemlark.com
      </li>
      <li class="contact__item">
        <svg class="contact__icon" viewBox="0 0 20 20" aria-hidden="true" fill="none" stroke="var(--brand-orange)" stroke-width="1.3">
          <circle cx="10" cy="10" r="8"/>
          <ellipse cx="10" cy="10" rx="3.5" ry="8"/>
          <path d="M2 10h16M3.5 6h13M3.5 14h13"/>
        </svg>
        www.tandemlark.com
      </li>
    </ul>
  </section>
</body>
</html>
```